Brightpath Health Flyer Design for Virtual Online Clinic. -5.5 x 8.5 inches (half sheet)

We need a clean, modern flyer design for Brightpath Health, a new virtual walk-in clinic based in British Columbia. The flyer will be used in libraries, pharmacies, and community centers to help residents easily access primary care through their Brightpath Health NFC access card.
The flyer will ask a question : NEED A DOCTOR? This should be large and attention grabbing.
The design should clearly feature a Brightpath Health card image (the access card) as the centerpiece and visually show how patients can use it to book appointments. The tone should feel trustworthy, healthcare-oriented, and community-friendly — clean fonts, clear spacing, and strong readability from a distance.

Side One: This card has the NFC Access Card.
NEED A DOCTOR? (Large Font, Attention Grabbing)
How to Book an Appointment using your Brightpath Health Card
Step 1: Tap Your Card on Your Phone
Hold your card near the back of your phone.
It will activate automatically — no app needed.
The Brightpath Health scheduler will open.
Step 2: Schedule Your Appointment
Select your clinical concern.
Choose your time window.
Register (only once).
Confirm your appointment.
Step 3: Relax, we’ll take care of the rest
A doctor will call during your scheduled time.
Once booked, you’ll be able to call our office.
No emails, no texts — just a real person.
It’s that simple.
Side Two:
About Brightpath Health
Created by Dr. Marcus Feldtree
Brightpath Health was founded to make healthcare simple and convenient. Prescription renewals. Common infections. Medical notes. And so much more.
Our doctors can address 120+ health concerns virtually — providing quality care without the waiting room. No waiting rooms. Just real doctors providing real care.
Why Patients Choose Brightpath Health
Easy access – book and be seen from anywhere in BC.
Effortless booking – tap your Brightpath Health Card to begin.
Trusted physicians – every visit is with a licensed BC family doctor.
How It Works
Book your visit — choose a time window that fits your day.
Join the queue — you’ll be called when it’s your turn.
Speak directly with your doctor — simple, secure, and stress-free.
Convenient Care for Common Concerns

Additional Details.
Please find the domain to be launched soon. I've attached the NFC card file for review, it is 85.5 mm x 54 mm. The card will be glued to the flyer.
I've attached examples of flyers but they are not the look I am seeking and I am looking for creative solutions.
Thank you!
http://brightpath-example.test/

Target Market(s)

Adult Patients in British Columbia

Industry/Entity Type

Healthcare

Font styles to use
Other font styles liked:
• Looking for clean lines, uniform appearance, and high legibility i.e poppins

Colors
0054AA
0677BA
7BADD7
CADEEF
E8F1F8

Requirements
Must have
• Need A Doctor?
Nice to have
• Elegant style, not too busy, clear layout.
Should not have
• Clutter, look cheap - review examples.

```html
<!DOCTYPE html>
<html lang="en">
<head>
<meta charset="utf-8">
<title>Brightpath Health Flyer</title>
<link href="https://fonts.googleapis.com/css2?family=Poppins:wght@300;400;500;600;700;800&display=swap" rel="stylesheet">
<style>
:root{
  --stage:#45be93;
  --navy-deep:#1b1f6b;
  --navy:#25409a;
  --royal:#2a3f94;
  --mint:#45be93;
  --ink:#1f2a44;
  --white:#ffffff;
  --paper:#f7f8fa;
}
*{box-sizing:border-box;margin:0;padding:0}
html,body{width:960px;height:1200px;overflow:hidden}
body{background:var(--stage);font-family:'Poppins',sans-serif;position:relative;color:var(--ink)}
.dims{position:absolute;left:0;top:0}
.dim-label{position:absolute;color:var(--white);font-size:22px;font-weight:400;font-family:'Poppins',sans-serif}

/* front */
.flyer-front{position:absolute;left:118px;top:100px;width:724px;height:468px;overflow:hidden;
  background:radial-gradient(ellipse at 60% 40%,#4a63d8 0%,#2b2fa4 35%,var(--navy-deep) 80%);
  box-shadow:0 6px 14px rgba(0,0,0,.25)}
.brand-top{position:absolute;left:0;right:0;top:26px;text-align:center;color:var(--white);font-size:17px;font-weight:500}
.tagline{position:absolute;left:26px;top:68px;color:var(--mint);font-size:15.5px;font-weight:400}
.headline{position:absolute;left:24px;top:96px;color:var(--white);font-size:46px;font-weight:800;letter-spacing:-.5px;line-height:1;white-space:nowrap}
.subhead{position:absolute;left:26px;top:157px;color:var(--white);font-size:17px;font-weight:400;line-height:1.2}
.subhead b{font-weight:700}
.step-line{position:absolute;left:37px;top:228px;width:2px;height:166px;background:var(--mint)}
.step-num{position:absolute;left:27px;width:21px;height:21px;border-radius:50%;background:var(--mint);color:var(--white);
  font-size:11px;font-weight:600;display:flex;align-items:center;justify-content:center;box-shadow:0 0 0 3px rgba(69,190,147,.3)}
.step-pill{position:absolute;left:62px;height:20px;border-radius:10px;background:var(--white);color:var(--navy);
  font-size:11px;font-weight:700;padding:0 12px;display:flex;align-items:center}
.step-body{position:absolute;left:62px;color:var(--white);font-size:8.6px;line-height:1.25;font-weight:400}
.card-in-hand{position:absolute;left:464px;top:89px;width:242px;height:379px;border-radius:10px 10px 0 0;
  background:linear-gradient(170deg,#dfe4f3 0%,#c9d0ea 30%,#d9ad90 65%,#c58f70 100%);opacity:.85}
.phone-shot{position:absolute;left:344px;top:156px;width:178px;height:320px;border-radius:28px;
  border:5px solid #0f1222;background:linear-gradient(180deg,#2f4a9e 0%,#2f4a9e 18%,#eef2fa 19%,#e6ebf6 85%,#2f4a9e 86%)}

/* back */
.flyer-back{position:absolute;left:118px;top:631px;width:724px;height:469px;background:var(--paper);overflow:hidden;
  box-shadow:0 6px 14px rgba(0,0,0,.2)}
.sec-title{position:absolute;left:26px;color:var(--navy);font-size:15.5px;font-weight:700;padding-left:13px;border-left:3px solid var(--mint);line-height:1.2}
.portrait{position:absolute;left:27px;top:55px;width:75px;height:75px;border-radius:50%;border:3px solid var(--mint);
  background:linear-gradient(160deg,#c9ccd4,#8e96a8)}
.created{position:absolute;left:113px;top:72px;font-size:17px;line-height:1.15;color:var(--ink)}
.created b{display:block;color:var(--navy);font-weight:700}
.about-copy{position:absolute;left:26px;top:140px;width:350px;font-size:8.7px;line-height:1.23;color:var(--ink)}
.reason{position:absolute;left:26px;display:flex;align-items:center;gap:6px;font-size:8.8px}
.reason b{color:var(--navy);font-size:11.5px;font-weight:700}
.flow-line{position:absolute;left:68px;top:374px;width:240px;height:2px;background:var(--mint)}
.flow-icon{position:absolute;top:358px;width:33px;height:33px;border-radius:50%;background:var(--mint);display:flex;align-items:center;justify-content:center}
.flow-step{position:absolute;text-align:center;width:140px}
.flow-step b{display:block;color:var(--navy);font-size:11.5px;font-weight:700;line-height:1.2}
.flow-step span{display:block;font-size:7.3px;line-height:1.2;margin-top:2px}

.card{position:absolute;left:399px;width:298px;height:170px;border-radius:14px;overflow:hidden;box-shadow:0 3px 8px rgba(0,0,0,.25)}
.card-front{top:50px;background:var(--white)}
.card-band{position:absolute;left:0;top:0;width:86px;height:100%;background:var(--royal)}
.card-chip{position:absolute;right:18px;top:15px;width:12px;height:12px;background:var(--royal);border-radius:2px}
.card-name{position:absolute;left:96px;right:8px;top:70px;text-align:center;color:var(--royal);font-size:18px;font-weight:600;white-space:nowrap}
.card-tap{position:absolute;right:16px;bottom:16px;display:flex;align-items:center;gap:8px;color:var(--royal);font-size:9.5px}
.card-back{top:248px;background:var(--royal)}
.card-back .card-name{left:0;right:0;top:58px;color:var(--white);font-size:22px}
.card-url{position:absolute;left:0;right:0;top:99px;text-align:center;color:var(--white);font-size:9.5px;letter-spacing:.5px}
</style>
</head>
<body>

<svg class="dims" width="960" height="1200" aria-hidden="true">
  <g stroke="#fff" stroke-width="1.2" fill="none">
    <line x1="118" y1="55" x2="448" y2="55"/><line x1="512" y1="55" x2="842" y2="55"/>
    <line x1="118" y1="39" x2="118" y2="71"/><line x1="842" y1="39" x2="842" y2="71"/>
    <line x1="887" y1="100" x2="887" y2="302"/><line x1="887" y1="366" x2="887" y2="568"/>
    <line x1="871" y1="100" x2="903" y2="100"/><line x1="871" y1="568" x2="903" y2="568"/>
    <line x1="887" y1="681" x2="887" y2="736"/><line x1="887" y1="800" x2="887" y2="852"/>
    <line x1="871" y1="681" x2="903" y2="681"/><line x1="871" y1="852" x2="903" y2="852"/>
    <line x1="887" y1="879" x2="887" y2="932"/><line x1="887" y1="995" x2="887" y2="1048"/>
    <line x1="871" y1="879" x2="903" y2="879"/><line x1="871" y1="1048" x2="903" y2="1048"/>
    <line x1="517" y1="1146" x2="633" y2="1146"/><line x1="698" y1="1146" x2="815" y2="1146"/>
    <line x1="517" y1="1130" x2="517" y2="1162"/><line x1="815" y1="1130" x2="815" y2="1162"/>
  </g>
</svg>
<div class="dim-label" style="left:460px;top:38px">8.5″</div>
<div class="dim-label" style="left:866px;top:316px">5.5″</div>
<div class="dim-label" style="left:876px;top:752px">2″</div>
<div class="dim-label" style="left:876px;top:948px">2″</div>
<div class="dim-label" style="left:648px;top:1130px">3.5″</div>

<section class="flyer-front">
  <div class="card-in-hand" role="img" aria-label="Hand holding a Brightpath Health access card"></div>
  <div class="phone-shot" role="img" aria-label="Phone showing the Brightpath Health booking screen"></div>
  <div class="brand-top">Brightpath Health</div>
  <p class="tagline">This card has the NFC Access Card.</p>
  <h1 class="headline">NEED A DOCTOR?</h1>
  <p class="subhead">How to <b>Book an Appointment</b><br>using your Brightpath Health Card</p>

  <div class="step-line"></div>
  <div class="step-num" style="top:217px">1</div>
  <div class="step-pill" style="top:217px">Tap Your Card on Your Phone</div>
  <p class="step-body" style="top:244px">Hold your card near the back of your phone.<br>It will activate automatically — no app needed.<br>The Brightpath Health scheduler will open.</p>

  <div class="step-num" style="top:294px">2</div>
  <div class="step-pill" style="top:294px">Schedule your appointment</div>
  <p class="step-body" style="top:321px">Select your clinical concern.<br>Choose your time window.<br>Register (only once).<br>Confirm your appointment.</p>

  <div class="step-num" style="top:382px">3</div>
  <div class="step-pill" style="top:382px">Relax, we’ll take care of the rest</div>
  <p class="step-body" style="top:410px">A doctor will call during your scheduled time.<br>Once booked, you’ll be able to call our office.<br>No emails, no texts — just a real person. It’s that simple.</p>
</section>

<section class="flyer-back">
  <h2 class="sec-title" style="top:27px">About Brightpath Health</h2>
  <div class="portrait" role="img" aria-label="Portrait of Dr. Marcus Feldtree"></div>
  <p class="created">Created by<b>Dr. Marcus Feldtree</b></p>
  <p class="about-copy">Brightpath Health was founded to make healthcare simple and convenient. Prescription renewals. Common infections. Medical notes. And so much more. Our doctors can address 120+ health concerns virtually — providing quality care without the waiting room. No waiting rooms. Just real doctors providing real care.</p>

  <h2 class="sec-title" style="top:208px">Why Patients Choose Brightpath Health</h2>
  <div class="reason" style="top:240px"><svg width="17" height="17" viewBox="0 0 17 17"><circle cx="8.5" cy="8.5" r="7.5" fill="none" stroke="#45be93" stroke-width="1.5"/><path d="M5 8.7l2.4 2.3 4.6-4.7" fill="none" stroke="#45be93" stroke-width="1.6"/></svg><b>Easy access</b> – book and be seen from anywhere in BC.</div>
  <div class="reason" style="top:265px"><svg width="17" height="17" viewBox="0 0 17 17"><circle cx="8.5" cy="8.5" r="7.5" fill="none" stroke="#45be93" stroke-width="1.5"/><path d="M5 8.7l2.4 2.3 4.6-4.7" fill="none" stroke="#45be93" stroke-width="1.6"/></svg><b>Effortless booking</b> – tap your Brightpath Health Card to begin</div>
  <div class="reason" style="top:290px"><svg width="17" height="17" viewBox="0 0 17 17"><circle cx="8.5" cy="8.5" r="7.5" fill="none" stroke="#45be93" stroke-width="1.5"/><path d="M5 8.7l2.4 2.3 4.6-4.7" fill="none" stroke="#45be93" stroke-width="1.6"/></svg><b>Trusted physicians</b> – every visit is with a licensed BC family doctor.</div>

  <h2 class="sec-title" style="top:323px">How It Works</h2>
  <div class="flow-line"></div>
  <div class="flow-icon" style="left:52px"><svg width="17" height="17" viewBox="0 0 17 17"><rect x="2" y="3" width="13" height="12" rx="1.5" fill="#25409a"/><rect x="2" y="3" width="13" height="3" fill="#1b2f7a"/><path d="M5.5 10l2 2 4-4" fill="none" stroke="#fff" stroke-width="1.4"/></svg></div>
  <div class="flow-icon" style="left:167px"><svg width="19" height="19" viewBox="0 0 19 19"><circle cx="9.5" cy="9.5" r="7" fill="none" stroke="#25409a" stroke-width="2"/><path d="M9.5 5.5v4.2l2.8 1.8" fill="none" stroke="#25409a" stroke-width="1.8"/></svg></div>
  <div class="flow-icon" style="left:293px"><svg width="17" height="17" viewBox="0 0 17 17"><circle cx="8.5" cy="5" r="3.2" fill="#25409a"/><path d="M2.5 16c0-4 2.7-6 6-6s6 2 6 6z" fill="#25409a"/></svg></div>

  <div class="flow-step" style="left:-2px;top:399px"><b>Book your visit</b><span>Choose a time window<br>that fits your day.</span></div>
  <div class="flow-step" style="left:113px;top:399px"><b>Join the queue</b><span>you’ll be called when<br>it’s your turn.</span></div>
  <div class="flow-step" style="left:222px;top:399px;width:174px"><b>Speak directly<br>with your doctor</b><span>Simple, Secure, and Stress-Free.<br>Convenient Care for Common Concerns</span></div>

  <div class="card card-front">
    <div class="card-band"></div>
    <div class="card-chip"></div>
    <div class="card-name">Brightpath Health</div>
    <div class="card-tap">Tap Here to Book
      <svg width="24" height="16" viewBox="0 0 24 16"><rect x="1" y="1" width="22" height="14" rx="3" fill="none" stroke="#2a3f94" stroke-width="1.3"/><rect x="4" y="5" width="6" height="6" rx="1" fill="#2a3f94"/><path d="M13 5a4 4 0 0 1 0 6M16 3.5a6 6 0 0 1 0 9" fill="none" stroke="#2a3f94" stroke-width="1.3"/></svg>
    </div>
  </div>
  <div class="card card-back">
    <div class="card-name">Brightpath Health</div>
    <div class="card-url">www.brightpath-example.test</div>
  </div>
</section>

</body>
</html>
```